Brightpath Letterhead

We would like a letterhead for our company. I have uploaded our logo.

Brightpath Ridge Consulting
1450 W Corliss Ave Ste 310
Mesquite Falls, TX 75290
833-517-2906

```html
<!DOCTYPE html>
<html lang="en">
<head>
<meta charset="utf-8">
<title>Brightpath Letterhead</title>
<link rel="stylesheet" href="https://fonts.googleapis.com/css2?family=Montserrat:wght@500;600;700&family=Arimo:wght@400;700&display=swap">
<style>
  :root {
    --teal-dark: #0a5e6a;
    --green: #6cc49a;
    --paper: #ffffff;
    --ink: #1a1a1a;
    --backdrop: #e4ecec;
  }
  * { box-sizing: border-box; margin: 0; padding: 0; }
  html, body { width: 1200px; height: 800px; overflow: hidden; }
  body {
    background: var(--backdrop);
    font-family: "Arimo", Arial, sans-serif;
    color: var(--ink);
  }
  .letterhead {
    position: absolute;
    left: 330px; top: 18px;
    width: 540px; height: 764px;
    background: var(--paper);
    box-shadow: 0 4px 18px rgba(0,0,0,0.12);
    overflow: hidden;
  }
  .brand-block {
    position: absolute;
    left: 0; top: 14px;
    width: 330px; height: 96px;
    background: var(--teal-dark);
    display: flex; align-items: center;
    padding-left: 30px; padding-right: 20px; gap: 10px;
  }
  .brand-mark {
    width: 22px; height: 22px; border-radius: 50%;
    background: var(--paper); flex: none;
  }
  .brand-name {
    font-family: "Montserrat", sans-serif;
    font-weight: 600;
    font-size: 15px;
    letter-spacing: 2px;
    text-transform: uppercase;
    color: var(--paper);
    line-height: 1.25;
  }
  .company-band {
    position: absolute;
    left: 330px; top: 62px;
    width: 210px; height: 30px;
    background: var(--green);
    display: flex; align-items: center; justify-content: center;
    font-family: "Montserrat", sans-serif;
    font-weight: 700; font-size: 11.5px;
    color: var(--paper);
    letter-spacing: 0.3px;
    white-space: nowrap;
  }
  .company-address {
    position: absolute;
    left: 345px; top: 104px;
    width: 185px;
    font-style: normal;
    font-size: 10.5px; line-height: 1.5;
    white-space: nowrap;
  }
  .company-address .phone { display: flex; align-items: center; gap: 5px; }
  .company-address svg { width: 10px; height: 10px; }
  .recipient {
    position: absolute;
    left: 60px; top: 150px;
    font-family: "Montserrat", sans-serif;
  }
  .recipient .label { font-weight: 700; font-size: 10px; }
  .recipient .name { font-weight: 700; font-size: 12px; letter-spacing: 1.5px; margin-top: 8px; }
  .letter-body {
    position: absolute;
    left: 60px; top: 212px; width: 420px;
  }
  .letter-body p {
    font-size: 10.5px; line-height: 2;
    margin-bottom: 14px;
  }
  .sign-off {
    position: absolute;
    left: 60px; top: 560px;
    font-family: "Montserrat", sans-serif;
    font-weight: 700; font-size: 13px; letter-spacing: 2px;
  }
  .footer-line {
    position: absolute;
    left: 0; bottom: 38px; width: 100%; height: 6px;
    background: var(--green);
  }
  .footer-bar {
    position: absolute;
    left: 0; bottom: 0; width: 100%; height: 28px;
    background: var(--teal-dark);
  }
</style>
</head>
<body>
  <main class="letterhead">
    <header>
      <div class="brand-block">
        <span class="brand-mark"></span>
        <span class="brand-name">Brightpath Ridge Consulting</span>
      </div>
      <div class="company-band">Brightpath Ridge Consulting</div>
      <address class="company-address">
        <div>1450 W Corliss Ave Ste 310</div>
        <div>Mesquite Falls, TX 75290</div>
        <div class="phone">
          <svg viewBox="0 0 24 24" aria-hidden="true"><path fill="#1a1a1a" d="M6.6 10.8a15.1 15.1 0 0 0 6.6 6.6l2.2-2.2c.3-.3.7-.4 1-.2 1.1.4 2.3.6 3.6.6.6 0 1 .4 1 1V20c0 .6-.4 1-1 1C10.6 21 3 13.4 3 4c0-.6.4-1 1-1h3.5c.6 0 1 .4 1 1 0 1.3.2 2.5.6 3.6.1.3 0 .7-.2 1z"/></svg>
          <span>833-517-2906</span>
        </div>
      </address>
    </header>

    <section class="recipient">
      <div class="label">To.</div>
      <div class="name">Mr. JOHN DOE</div>
    </section>

    <section class="letter-body">
      <p>Lorem Ipsum is simply dummy text of the printing and typesetting industry. Lorem Ipsum has been the industry's standard dummy text ever since the 1500s, when an unknown printer took a galley of type and scrambled it to make a type specimen book.</p>
      <p>Lorem Ipsum is simply dummy text of the printing and typesetting industry. Lorem Ipsum has been the industry's standard dummy text ever since the 1500s, when an unknown printer took a galley of type and scrambled it to make a type specimen book.</p>
    </section>

    <div class="sign-off">Regards,</div>

    <footer>
      <div class="footer-line"></div>
      <div class="footer-bar"></div>
    </footer>
  </main>
</body>
</html>
```